Fore Sale sign for my real estate agency

I am a Brisbane - Australia inner western suburbs boutique real estate agent who is needing a for sale sign. We are a small dynamic family agency that needs a for sale sign that will standout and give us a strong presence in the market.

I have attached a logo I like, however I am not fixed on anything and am open to suggestions.

The information on the sign should contain but not necessarily limited to the following information - please appreciate I am very open
1 logo - O'Venny
2 Ph number - 3847 1952
3 web address - ovenny.com.au

Thank you
Gareth O'Venny

```html
<!DOCTYPE html>
<html lang="en">
<head>
<meta charset="utf-8">
<title>O'Venny – For Sale Sign</title>
<link rel="stylesheet" href="https://fonts.googleapis.com/css2?family=Anton&family=Tinos:wght@700&display=swap">
<style>
  :root {
    --backdrop: #0b0b0b;
    --board: #ffffff;
    --sign-red: #e2001a;
    --headline: #ffffff;
    --outline: #000000;
    --phone-yellow: #fff200;
    --brand-ink: #2b2b2b;
    --ring-light: #f2f2f2;
    --ring-dark: #8a8a8a;
  }
  html, body {
    margin: 0;
    padding: 0;
    width: 1200px;
    height: 720px;
    overflow: hidden;
    background: var(--backdrop);
  }
  .sign {
    display: block;
    width: 1200px;
    height: 720px;
  }
  .headline {
    font-family: "Anton", "Impact", sans-serif;
    font-size: 215px;
    fill: var(--headline);
    stroke: var(--outline);
    stroke-width: 7px;
    paint-order: stroke fill;
    letter-spacing: 2px;
  }
  .call-now {
    font-family: "Tinos", "Times New Roman", serif;
    font-weight: 700;
    font-size: 50px;
    fill: var(--headline);
  }
  .phone {
    font-family: "Anton", "Impact", sans-serif;
    font-size: 92px;
    fill: var(--phone-yellow);
    letter-spacing: 1px;
  }
  .web {
    font-family: "Tinos", "Times New Roman", serif;
    font-size: 40px;
    fill: var(--headline);
  }
  .brand-name {
    font-family: "Anton", "Impact", sans-serif;
    font-size: 76px;
    fill: var(--brand-ink);
    letter-spacing: 3px;
  }
</style>
</head>
<body>
<svg class="sign" viewBox="0 0 1200 720" xmlns="http://www.w3.org/2000/svg">
  <defs>
    <linearGradient id="ring-shade" x1="0" y1="0" x2="0" y2="1">
      <stop offset="0" stop-color="var(--ring-light)"/>
      <stop offset="0.5" stop-color="var(--ring-dark)"/>
      <stop offset="1" stop-color="var(--ring-light)"/>
    </linearGradient>
  </defs>

  <rect class="board" x="163" y="68" width="870" height="580" fill="var(--board)"/>

  <polygon class="sign-panel" fill="var(--sign-red)"
    points="223,78 968,78 1023,128 1023,518 713,518 713,640 240,640 173,590 173,128"/>

  <ellipse class="headline-ring" cx="602" cy="262" rx="302" ry="150"
    fill="none" stroke="url(#ring-shade)" stroke-width="9"/>

  <text class="headline" x="600" y="350" text-anchor="middle">FOR SALE</text>

  <text class="call-now" x="213" y="470">CALL NOW</text>
  <text class="phone" x="208" y="565">3847 1952</text>
  <text class="web" x="213" y="600">www.ovenny.com.au</text>

  <text class="brand-name" x="868" y="612" text-anchor="middle">O'VENNY</text>
</svg>
</body>
</html>
```